Corwin Teshale, MD Print Package_Trifold

Need a trifold brochure designed. The business is a cosmetic surgery office with cosmetic procedures involving face surgery, body surgery, breast surgery, and skin care treatments. At this point, we would like to see a brochure with some more white space.

A little bit about the doctor for character reference:
Dr. Corwin Teshale believes the art of cosmetic surgery is in listening to his patients. He builds each treatment plan on a solid foundation of communication between doctor and patient and spends a considerable amount of time getting to know the people he treats — taking their goals into account and offering the best options to meet those goals. At our state-of-the-art Brightvale Cosmetic Surgery, you are not just a patient; You are our guest.

Their website for further information and for color scheme reference, as the client would like the brochure to match his website (ie: ocean blue/teal, grays and black), is http://www.drcorwinteshale.example/

Attached is a brochure that the client created a few months back. This shows a general idea of how he would like the layout to be and the information to put on the trifold.

Also Attached are two additional Before & Afters for the brochure, per the client's request. As well as a picture of the Pelora Beam machine that performs these procedures.

Also attached is a brochure intake document for further guidelines as well.
Updates

Reason: Didn't receive enough *differing designs* - would like to see at least 3 others.

Industry/Entity Type

Business

Requirements
Must have
• If utilizing any staff photos - please be sure to use Dr. Corwin Teshale, you can find him here:
• http://www.drcorwinteshale.example/about

```html
<!DOCTYPE html>
<html lang="en">
<head>
<meta charset="utf-8">
<title>Corwin Teshale, MD – Trifold Inside</title>
<link rel="stylesheet" href="https://fonts.googleapis.com/css2?family=Titillium+Web:ital,wght@0,300;0,400;0,600;0,700;1,300;1,400;1,700&display=swap">
<style>
  :root {
    --page: #e6e9eb;
    --paper: #ffffff;
    --teal-deep: #56798a;
    --teal-mid: #6f93a3;
    --teal-light: #9dbdcc;
    --teal-sky: #86b8cf;
    --label: #5b7f8f;
    --address: #4f7585;
    --machine-title: #6b8d9c;
    --text-light: #ffffff;
    --skin-dark: #8a5a44;
    --skin-mid: #c79a85;
    --skin-light: #e6c3b2;
  }
  * { box-sizing: border-box; margin: 0; padding: 0; }
  html, body { width: 1200px; height: 1000px; overflow: hidden; }
  body { background: var(--page); font-family: "Titillium Web", sans-serif; position: relative; }

  .brochure { position: absolute; left: 72px; top: 95px; width: 1056px; height: 810px; display: flex; box-shadow: 0 4px 14px rgba(0,0,0,.18); }
  .panel { position: relative; height: 810px; overflow: hidden; background: var(--paper); }
  .panel--left { width: 353px; }
  .panel--middle { width: 348px; background: linear-gradient(180deg, #f3f5f6 0%, #dfe7eb 30%, #a9c7d6 75%, var(--teal-sky) 100%); }
  .panel--right { width: 355px; }
  .panel-wave { position: absolute; left: 0; top: 0; width: 100%; height: 100%; }

  .tag { position: absolute; width: 69px; height: 22px; background: var(--label); color: var(--text-light);
         font-style: italic; font-size: 13px; line-height: 22px; text-align: center; }
  .tag--light { background: #fff; color: var(--label); }

  .photo { position: absolute; border-radius: 0 18px 18px 0; }
  .photo--lips { left: 22px; top: 82px; width: 311px; height: 131px; background: linear-gradient(90deg, #6b4030 0%, var(--skin-dark) 48%, #b07e63 52%, var(--skin-mid) 100%); }
  .photo--belly { left: 22px; top: 420px; width: 311px; height: 131px; background: linear-gradient(90deg, #cdb3a6 0%, #d9c0b4 48%, #e2cfc4 52%, #ecdcd2 100%); }
  .photo--scar { left: 24px; top: 227px; width: 311px; height: 133px; background: linear-gradient(90deg, #a9675e 0%, #b57a6e 48%, #cfa196 52%, #d9afa3 100%); }
  .photo--tattoo { left: 24px; top: 557px; width: 311px; height: 133px; background: linear-gradient(90deg, #6f8a79 0%, #8aa08f 33%, #b9b7a8 34%, #c8bdae 66%, #d8cbc0 67%, #e1d4ca 100%); }
  .photo--rosacea { left: 20px; top: 335px; width: 312px; height: 63px; background: linear-gradient(90deg, #d9867b 0%, #e2a092 48%, #e3ae9e 52%, #eac2b3 100%); }
  .photo--freckles { left: 28px; top: 565px; width: 295px; height: 70px; background: linear-gradient(90deg, #d9a48e 0%, #e3b7a3 48%, #eccbbb 52%, #f1d8cb 100%); }
  .photo--machine { left: 56px; top: 8px; width: 115px; height: 277px; border-radius: 8px; background: linear-gradient(180deg, #e4e7ea 0%, #c5cace 55%, #9aa1a7 100%); }

  .title { position: absolute; color: var(--text-light); font-weight: 700; font-style: italic; font-size: 14.5px; letter-spacing: .2px; text-transform: uppercase; }
  .body-copy { position: absolute; color: var(--text-light); font-size: 12px; line-height: 17.6px; text-align: justify; }
  .panel--left .title, .panel--left .body-copy { left: 22px; width: 311px; }
  .panel--middle .title, .panel--middle .body-copy { left: 24px; width: 312px; }
  .panel--right .title, .panel--right .body-copy { left: 22px; width: 312px; }

  .pin { position: absolute; left: 163px; top: 36px; }
  .address { position: absolute; left: 0; width: 348px; text-align: center; color: var(--address); font-size: 12px; line-height: 17px; text-transform: uppercase; letter-spacing: .2px; }

  .machine-name { position: absolute; left: 177px; top: 118px; color: var(--machine-title); font-weight: 300; font-style: italic; font-size: 27px; line-height: 34px; }

  .web-pill { position: absolute; left: 24px; top: 755px; height: 26px; padding: 0 11px 0 8px; background: #fff; border-radius: 8px;
              display: flex; align-items: center; gap: 6px; color: var(--address); font-style: italic; font-size: 13px; }
</style>
</head>
<body>
<main class="brochure">

  <section class="panel panel--left">
    <svg class="panel-wave" viewBox="0 0 353 810" preserveAspectRatio="none" aria-hidden="true">
      <defs>
        <linearGradient id="waveLeft" x1="0" y1="0" x2="0" y2="1">
          <stop offset="0" stop-color="#56798a"/>
          <stop offset=".55" stop-color="#6f93a3"/>
          <stop offset="1" stop-color="#9dbdcc"/>
        </linearGradient>
      </defs>
      <path d="M0,225 C110,250 240,205 353,180 L353,810 L0,810 Z" fill="url(#waveLeft)"/>
    </svg>

    <span class="tag" style="left:67px; top:45px;">Before</span>
    <span class="tag" style="left:222px; top:45px;">After</span>
    <div class="photo photo--lips" role="img" aria-label="Before and after photos of the upper lip area following laser hair removal"></div>
    <h2 class="title" style="top:228px;">Laser Hair Removal</h2>
    <p class="body-copy" style="top:250px;">Are you tired of shaving, waxing, tweezing, and plucking? Laser hair removal provides a fast, easy solution for permanent hair reduction, allowing you to look and feel your best without all the hassle. Popular areas for treatment are the lower face, upper lip, underarms, chest, back, bikini and legs. Fees are based on area.</p>

    <span class="tag tag--light" style="left:67px; top:383px;">Before</span>
    <span class="tag tag--light" style="left:222px; top:383px;">After</span>
    <div class="photo photo--belly" role="img" aria-label="Before and after photos of abdominal stretch marks"></div>
    <h2 class="title" style="top:568px;">Stretch Marks</h2>
    <p class="body-copy" style="top:590px;">80% of women and 40% of men have stretch marks. We have the only non-ablative fractional treatment that is FDA approved to minimize the appearance of stretch marks associated with pregnancy, hormonal changes and weight gain. It works by using fractional laser light to break down stretch marks and naturally trigger healthy, new tissue growth, including collagen. Fees are based on the size of the area being treated.</p>

    <div class="web-pill">
      <svg width="14" height="14" viewBox="0 0 14 14" aria-hidden="true" fill="none" stroke="#4f7585" stroke-width="1">
        <circle cx="7" cy="7" r="6"/><ellipse cx="7" cy="7" rx="2.6" ry="6"/><path d="M1,7 H13 M2,3.8 H12 M2,10.2 H12"/>
      </svg>
      <span>www.drcorwinteshale.example</span>
    </div>
  </section>

  <section class="panel panel--middle">
    <svg class="pin" width="22" height="22" viewBox="0 0 22 22" aria-hidden="true">
      <path d="M11,2 C7,2 4.5,5 4.5,8.5 C4.5,13 11,20 11,20 C11,20 17.5,13 17.5,8.5 C17.5,5 15,2 11,2 Z" fill="#5b7f8f"/>
      <circle cx="11" cy="8.5" r="2.4" fill="#eef2f4"/>
    </svg>
    <p class="address" style="top:70px;">Brightvale Cosmetic Surgery<br>1 Harborline Drive Ste 301, Newark, DE 19713</p>
    <p class="address" style="top:110px;">Lumen Faces Aesthetic Center 34172<br>Meadowbrook Drive, Lewes, DE 19958</p>

    <span class="tag" style="left:68px; top:190px;">Before</span>
    <span class="tag" style="left:224px; top:190px;">After</span>
    <div class="photo photo--scar" role="img" aria-label="Before and after photos of a surgical scar treated with laser"></div>
    <h2 class="title" style="top:379px;">Surgical &amp; Acne Scars</h2>
    <p class="body-copy" style="top:402px;">Imagine yourself with beautiful skin that's free of scars. No more cover-up, extra clothing, or added daily expenses. With laser treatment for scar removal, unwanted scars can be a thing of the past. Laser scar removal is a non-invasive, advanced approach to scar treatment that offers excellent results without the discomfort and downtime of surgery.</p>

    <span class="tag tag--light" style="left:68px; top:520px;">Before</span>
    <span class="tag tag--light" style="left:224px; top:520px;">After</span>
    <div class="photo photo--tattoo" role="img" aria-label="Three photos showing a tattoo fading over successive laser treatments"></div>
    <h2 class="title" style="top:704px;">Tattoo Removal</h2>
    <p class="body-copy" style="top:726px;">Tattoo regret is experienced by many people, due to employment concerns, relationship status, and overall person growth and life changes. Thankfully we obtain state of the art laser technology that</p>
  </section>

  <section class="panel panel--right">
    <svg class="panel-wave" viewBox="0 0 355 810" preserveAspectRatio="none" aria-hidden="true">
      <defs>
        <linearGradient id="waveRight" x1="0" y1="0" x2="0" y2="1">
          <stop offset="0" stop-color="#5d8596"/>
          <stop offset=".6" stop-color="#7297a7"/>
          <stop offset="1" stop-color="#89adbd"/>
        </linearGradient>
      </defs>
      <path d="M0,285 C110,300 240,250 355,210 L355,810 L0,810 Z" fill="url(#waveRight)"/>
    </svg>

    <div class="photo photo--machine" role="img" aria-label="Pelora Beam laser machine on a wheeled cart"></div>
    <p class="machine-name">Pelora<br>Beam<br>Machine</p>

    <span class="tag tag--light" style="left:64px; top:307px;">Before</span>
    <span class="tag tag--light" style="left:219px; top:307px;">After</span>
    <div class="photo photo--rosacea" role="img" aria-label="Before and after photos of rosacea redness on the nose and cheeks"></div>
    <h2 class="title" style="top:405px;">Rosacea &amp; Vessels</h2>
    <p class="body-copy" style="top:427px;">IPL treatment can reduce rosacea redness and "flushing" to reveal clearer, more natural-looking skin in just a few easy treatments, providing a more permanent result than topical creams. Treatment can reduce rash, redness, flushing, acne-like papules, pustules, and patches, inflammation and broken vessels.</p>

    <span class="tag tag--light" style="left:64px; top:537px;">Before</span>
    <span class="tag tag--light" style="left:219px; top:537px;">After</span>
    <div class="photo photo--freckles" role="img" aria-label="Before and after photos of facial pigmentation and freckles"></div>
    <h2 class="title" style="top:643px;">Pigmentation</h2>
    <p class="body-copy" style="top:666px;">For those of us who've spent too much time in the sun, signs of premature aging may be more prominent than we'd like. Laser treatment can clear away skin discoloration and unwanted pigment to reveal more beautiful skin and give you a more revitalized appearance. Commonly called, Photofacials, this treatment treats age spots, sun damage, birthmarks, melasma and freckles. Fees are based on area treated such as spot treatment or full face treatment.</p>
  </section>

</main>
</body>
</html>
```